Coldforge Prime manufacturing Project

We are looking at getting a brand new design for a new company that deals in selling stainless tubing and other stainless still products such as handrails, Spigots, Balustrade Fittings
Glass, Glass fittings and Aluminium Channels

We require a very clean website that deals with the following colours:

Blue to light blues
Blacks
Greys to light Greys
Whites

We are open for other ideas BUT we *DO NOT* want any pinks, greens or bright colours except for backgrounds colours we have chosen above. (It can be solid, gradient or a subtle pattern)

YOU MUST KEEP THE LOGO AS IS. PLEASE DO NOT ALTER THE LOGO IN *ANY WAY* and the logo MUST be the same colours and fonts.

Logo is attached.

The site must contain these aspects:
jQuery Slider (Image slide show)
Top drop down Menus
Be no more than 900px wide
Text is to be to the w3C standards. (no special fonts)

We will chop up the design into html format. You just need to provide the PSD file.

The clients opposition is:
www.quorvatrim.example

Industry/Entity Type

It Company

Requirements
Nice to have
• Alter the logo in anyway

Files

```html
<!DOCTYPE html>
<html lang="en">
<head>
<meta charset="utf-8">
<title>Coldforge Prime Manufacturing</title>
<link href="https://fonts.googleapis.com/css2?family=Open+Sans:wght@300;400;600&family=Arimo:wght@400;700&family=Tinos:wght@400&display=swap" rel="stylesheet">
<style>
:root{
  --blue-dark:#0b3d73;
  --blue:#1d5a96;
  --blue-mid:#3f6f9e;
  --grey-bg:#f2f1f3;
  --ink:#1b1b1b;
  --white:#ffffff;
  --footer:#333333;
  --footer-text:#dddddd;
}
*{box-sizing:border-box;margin:0;padding:0}
html,body{width:1115px;height:1200px;overflow:hidden}
body{position:relative;background:var(--grey-bg);font-family:'Arimo',Arial,sans-serif;color:var(--ink)}
.abs{position:absolute}
.header{left:0;top:0;width:1115px;height:130px;background:linear-gradient(#f4f4f6,#ebebee)}
.brand-dot{left:104px;top:44px;width:40px;height:40px;border-radius:50%;background:var(--blue-dark)}
.brand-name{left:154px;top:51px;font-family:'Open Sans',sans-serif;font-weight:600;font-size:19px;line-height:26px;color:var(--blue-dark);white-space:nowrap}
.call-icon{left:744px;top:22px;width:29px;height:29px;background:var(--blue)}
.call{left:782px;top:31px;font-family:'Open Sans',sans-serif;font-size:17px;color:var(--blue-dark)}
.call span{color:#555}
.email{left:783px;top:55px;font-family:'Open Sans',sans-serif;font-size:13px;color:var(--blue-dark)}
.email span{color:#555}
.social{top:85px;width:30px;height:30px;border-radius:4px;background:var(--blue-mid)}
.nav{left:0;top:130px;width:1115px;height:45px;background:linear-gradient(#2a6aa6,#0e4684 55%,#0b3b70)}
.nav-strip{left:0;top:167px;width:1115px;height:8px;background:#1f5a94;border-top:1px solid #6d97c2}
.nav a{position:absolute;top:13px;transform:translateX(-50%);font-family:'Open Sans',sans-serif;font-size:12px;color:var(--white);text-decoration:none;letter-spacing:.3px;white-space:nowrap}
.nav i{position:absolute;top:6px;width:1px;height:30px;background:#4c7bb0}
.dropdown{left:383px;top:175px;width:147px;height:76px;background:var(--blue-mid);border-radius:0 0 6px 6px}
.dropdown .item{position:absolute;left:5px;width:137px;height:24px;padding-left:25px;line-height:24px;font-family:'Open Sans',sans-serif;font-size:13px;color:var(--white)}
.dropdown .active{top:10px;background:#f1f1f3;color:#111;border-radius:6px}
.welcome{left:100px;top:243px;font-family:'Open Sans',sans-serif;font-size:22px;font-weight:400;color:#959595;white-space:nowrap}
.welcome b{font-weight:400;color:var(--blue-dark)}
.rule{left:100px;top:282px;width:439px;border-top:1px dashed #b5b5b5}
.intro{left:101px;top:296px;width:450px;font-size:11px;line-height:16.7px;text-align:justify;color:#222}
.read-more{left:381px;top:427px;width:135px;height:37px;border-radius:7px;background:linear-gradient(#444,#0c0c0c);color:#fff;font-family:'Tinos',serif;font-size:17px;line-height:37px;text-align:center;box-shadow:0 2px 3px rgba(0,0,0,.35)}
.slider{left:587px;top:184px;width:418px;height:279px;background:#fff;border:1px solid #cfcfcf;box-shadow:0 1px 3px rgba(0,0,0,.2);padding:3px}
.slide{width:100%;height:100%;position:relative;background:linear-gradient(110deg,#d9ebe8,#b9d2d0 45%,#8d9aa3 60%,#e4eeee)}
.caption{position:absolute;left:0;bottom:0;width:100%;height:33px;background:rgba(60,110,160,.88);color:#fff;font-family:'Open Sans',sans-serif;font-size:16px;line-height:33px;text-align:center;letter-spacing:.3px}
.dot{top:476px;width:9px;height:9px;border-radius:50%;background:#d3d5db}
.dot.on{background:var(--blue-dark)}
.band{left:0;top:498px;width:1115px;height:542px;background:linear-gradient(#e6e6e8,var(--grey-bg) 8px)}
.sec-title{font-family:'Open Sans',sans-serif;font-size:20px;font-weight:400;color:#999;white-space:nowrap}
.sec-title b{font-weight:400;color:var(--blue-dark)}
.panel{background:#fff;border-radius:6px;box-shadow:0 0 3px rgba(0,0,0,.08)}
.thumb{width:151px;height:145px;border:3px solid #eee;background:linear-gradient(135deg,#f6f6f6,#b9b9bb 55%,#efefef)}
.tag{width:151px;height:25px;color:#fff;font-size:11px;font-weight:700;line-height:25px;padding-left:30px;white-space:nowrap}
.tag::before{content:"";position:absolute;left:6px;top:4px;width:17px;height:17px;border-radius:50%;background:#ddd}
.tag::after{content:"";position:absolute;left:12px;top:9px;border-left:6px solid #333;border-top:4px solid transparent;border-bottom:4px solid transparent}
.tag.blue{background:var(--blue)}
.tag.black{background:linear-gradient(90deg,#222,#000)}
.cat-img{left:177px;top:850px;width:72px;height:77px;background:linear-gradient(160deg,#c9cfd6,#8a7a5c 60%,#6d7a8a);transform:skewY(-4deg);box-shadow:2px 3px 4px rgba(0,0,0,.3)}
.cat-text{left:104px;top:943px;width:220px;text-align:center;font-size:12px;color:var(--blue-mid)}
.cat-text b{font-weight:400;color:#111}
.cat-btn{left:136px;top:972px;width:151px;height:25px;background:var(--blue-dark);color:#fff;font-size:11px;font-weight:700;line-height:25px;text-align:center}
.np-img{top:851px;width:152px;height:116px;border:1px solid var(--blue-dark);background:linear-gradient(135deg,#eef0f2,#9a6c60 45%,#dcdfe3)}
.np-label{top:980px;width:152px;text-align:center;font-size:11px;font-weight:700}
.arrow{top:889px;width:20px;height:20px;border-radius:50%;background:linear-gradient(#f3f3f3,#cfcfcf);border:1px solid #bbb}
.footer{left:0;top:1040px;width:1115px;height:160px;background:var(--footer)}
.f-dot{left:148px;top:1096px;width:30px;height:30px;border-radius:50%;background:#777}
.f-name{left:186px;top:1100px;font-family:'Open Sans',sans-serif;font-weight:600;font-size:14px;line-height:22px;color:var(--footer-text);white-space:nowrap}
.f-links{left:379px;top:1100px;font-family:'Open Sans',sans-serif;font-size:11px;color:#fff;word-spacing:2px;white-space:pre}
.copy{left:379px;top:1138px;font-size:11px;color:#fff}
</style>
</head>
<body>
<header class="abs header"></header>
<div class="abs brand-dot"></div>
<div class="abs brand-name">Coldforge Prime</div>

<svg class="abs call-icon" viewBox="0 0 29 29" aria-label="Phone">
  <path d="M11 7h4v4h-2v7h2v4h-4c-2 0-3-3-3-7.5S9 7 11 7z" fill="#fff"/>
</svg>
<div class="abs call">CALL NOW : <span>+00 1234 567 890</span></div>
<div class="abs email">EMAIL : <span>info@coldforgeprime.example</span></div>
<div class="abs social" style="left:848px" aria-label="Video channel"></div>
<div class="abs social" style="left:892px" aria-label="Microblog"></div>
<div class="abs social" style="left:936px" aria-label="Social page"></div>
<div class="abs social" style="left:980px" aria-label="News feed"></div>

<nav class="abs nav">
  <a style="left:183px">HOME</a><i style="left:239px"></i>
  <a style="left:314px">ABOUT US</a><i style="left:381px"></i>
  <a style="left:452px">PRODUCTS</a><i style="left:525px"></i>
  <a style="left:601px">DOWNLOAD</a><i style="left:666px"></i>
  <a style="left:751px">ONLINE ENQUIRY</a><i style="left:827px"></i>
  <a style="left:902px">CONTACT US</a>
</nav>
<div class="abs nav-strip"></div>
<div class="abs dropdown">
  <div class="item active">Product 1</div>
  <div class="item" style="top:40px">Product 2</div>
</div>

<h1 class="abs welcome">WELCOME TO <b>COLDFORGE PRIME</b></h1>
<div class="abs rule"></div>
<div class="abs intro">
  <p>Lorem Ipsum is simply dummy text of the printing and typesetting industry. Lorem Ipsum has been the industry's standard dummy text ever since the 1500s, when an unknown printer<br>.</p>
  <p>It has survived not only five centuries, but also the leap into electronic typesetting, remaining essentially unchanged. It was popularised in the 1960s with the release of Letraset sheets containing Lorem Ipsum passages, and more recently with desktop publishing software like It has survived not only five centuries, but also the leap into electronic typesetting, remaining</p>
</div>
<div class="abs read-more">Read More</div>

<div class="abs slider">
  <div class="slide" role="img" aria-label="Stainless steel glass clamp on a railing post">
    <div class="caption">STAINLESS STEEL RAILING &amp; GLASS SYSTEM</div>
  </div>
</div>
<div class="abs dot on" style="left:756px"></div>
<div class="abs dot" style="left:775px"></div>
<div class="abs dot" style="left:795px"></div>
<div class="abs dot" style="left:814px"></div>

<div class="abs band"></div>
<h2 class="abs sec-title" style="left:110px;top:507px">Our <b>Products</b></h2>
<div class="abs panel" style="left:108px;top:550px;width:899px;height:211px"></div>

<div class="abs thumb" style="left:117px;top:564px" role="img" aria-label="Railing systems product photo"></div>
<div class="abs tag blue" style="left:117px;top:723px">Railing Systems</div>
<div class="abs thumb" style="left:297px;top:564px" role="img" aria-label="Glass system product photo"></div>
<div class="abs tag black" style="left:294px;top:723px">Glass system</div>
<div class="abs thumb" style="left:479px;top:564px" role="img" aria-label="Post and balustrade product photo"></div>
<div class="abs tag blue" style="left:479px;top:724px">Post &amp; Balustrade</div>
<div class="abs thumb" style="left:667px;top:564px" role="img" aria-label="Square tube fittings product photo"></div>
<div class="abs tag black" style="left:669px;top:725px">Square tube Fittings</div>
<div class="abs thumb" style="left:845px;top:564px" role="img" aria-label="Sliding door and canopy product photo"></div>
<div class="abs tag blue" style="left:847px;top:725px;padding-left:24px">Sliding door &amp; Conopy</div>

<div class="abs panel" style="left:104px;top:792px;width:220px;height:213px"></div>
<h2 class="abs sec-title" style="left:118px;top:799px;font-size:21px">Download <b>Catalogue</b></h2>
<div class="abs cat-img" role="img" aria-label="2013 product catalogue cover"></div>
<div class="abs cat-text">OUR <b>2013</b> CATALOGUE</div>
<div class="abs cat-btn">Download Now</div>

<div class="abs panel" style="left:336px;top:792px;width:673px;height:210px"></div>
<h2 class="abs sec-title" style="left:347px;top:802px">New <b>Products</b></h2>
<svg class="abs arrow" style="left:359px" viewBox="0 0 20 20" aria-label="Previous"><path d="M12 5l-5 5 5 5" fill="none" stroke="#333" stroke-width="2.5"/></svg>
<div class="abs np-img" style="left:408px" role="img" aria-label="Glass standoff fitting photo"></div>
<div class="abs np-label" style="left:411px">Railing Systems</div>
<div class="abs np-img" style="left:599px;background:linear-gradient(135deg,#cfd6d5,#777 50%,#bfc7c6)" role="img" aria-label="Sliding door roller fitting photo"></div>
<div class="abs np-label" style="left:607px">Railing Systems</div>
<div class="abs np-img" style="left:788px" role="img" aria-label="Glass standoff fitting photo"></div>
<div class="abs np-label" style="left:785px">Railing Systems</div>
<svg class="abs arrow" style="left:964px;top:891px" viewBox="0 0 20 20" aria-label="Next"><path d="M8 5l5 5-5 5" fill="none" stroke="#333" stroke-width="2.5"/></svg>

<footer class="abs footer"></footer>
<div class="abs f-dot"></div>
<div class="abs f-name">Coldforge Prime</div>
<div class="abs f-links">HOME    -    ABOUT US    -    PRODUCTS    -    DOWNLOAD    -    ONLINE ENQUIRY    -    CONTACT US</div>
<div class="abs copy">2013 Coldforge Prime. All Rights Reserved.</div>
</body>
</html>
```